Alaska Personal Injury Lawyer needs a cover for a book

We need a cover for a 90 page paperback book. We want the cover to reflect a positive result coming out of a negative situation.

More specifically, this book discusses the process for maximizing one's personal injury claim arising from automobile accidents.

We are not looking for covers that show pictures of wrecked cars, ambulances or people in wheelchairs. We prefer for the cover to show people who have gotten past their injuries and the legal process and are happy again. Much like many pharmaceutical companies do. They advertise medicines that help horrible conditions, but instead of talking or showing the horrible disease, they show the happy outcome of getting better.

The title of the book with be:
Sunrise Over Quiet Fields
Steering Through Every Crash Claim

I am uploading a book cover on the same topic by someone else who successfully struck a balance between a bad situation and a positive outcome.

It's up to you whether to do an entirely positive cover vs a hybrid such as the one attached. However, the design should communicate more happiness and joy than fear and worry.

Thank you!

Target Market(s)

people who have been injured in car accidents that were not their fault

Industry/Entity Type

Legal

Font styles to use
Serif

Requirements
Must have
• We want the cover to reflect a positive result coming out of a negative situation.
• More specifically, this book discusses the process for maximizing one's personal injury claim arising from automobile accidents.
• We prefer for the cover to show people who have gotten past their injuries and the legal process and are happy again. Much like many pharmaceutical companies do. They advertise medicines that help horrible conditions, but instead of talking or showing the horrible disease, they show the happy outcome of getting better or people enjoying life, playing with kids and family.
• It's up to you whether to do an entirely positive cover vs a hybrid such as the one attached. However, the design should communicate more happiness and joy than fear and worry.
Nice to have
• Since the title is "Sunrise Over Quiet Fields: Steering Through Every Crash Claim" you might consider a nautical theme, but I encourage you to draw on your own creativity.
Should not have
• We are not looking for covers that show pictures of wrecked cars, ambulances or people in wheelchairs.
• The title of the book with be:
• Sunrise Over Quiet Fields
• Successfully Steering Through Every Crash Claim
• I am uploading a book cover on the same topic by someone else who successfully struck a balance between a bad situation and a positive outcome.

```html
<!DOCTYPE html>
<html lang="en">
<head>
<meta charset="utf-8">
<title>Sunrise Over Quiet Fields – Book Cover</title>
<link rel="stylesheet" href="https://fonts.googleapis.com/css2?family=Cinzel:wght@500;600&family=EB+Garamond:wght@500;600&display=swap">
<style>
  :root {
    --page-bg: #ffffff;
    --storm-dark: #17172e;
    --storm-mid: #433a5e;
    --storm-light: #9a93ad;
    --panel-cream: #fbf8e6;
    --title-navy: #132c4a;
    --title-blue: #1f4a78;
    --ink-dark: #1d2333;
    --sun-gold: #f6dfa0;
    --sun-peach: #efc9a4;
    --sky-clear: #c9d3e6;
    --interior-mid: #7b7fa8;
    --interior-deep: #3a3d68;
    --author-white: #f6f6fa;
  }
  html, body {
    margin: 0;
    padding: 0;
    width: 1200px;
    height: 1200px;
    overflow: hidden;
    background: var(--page-bg);
  }
  .cover {
    position: absolute;
    left: 214px;
    top: 0;
    width: 772px;
    height: 1200px;
    overflow: hidden;
    background: var(--interior-deep);
    box-shadow: 0 0 40px rgba(0, 0, 0, 0.25);
  }
  .storm-sky {
    position: absolute;
    left: 0;
    right: 0;
    top: 0;
    height: 760px;
    background: linear-gradient(180deg, var(--storm-dark) 0%, var(--storm-mid) 30%, var(--storm-light) 58%, var(--sky-clear) 78%, var(--sun-peach) 100%);
  }
  .title-panel {
    position: absolute;
    left: 74px;
    top: 0;
    width: 624px;
    height: 730px;
    background: linear-gradient(180deg, var(--panel-cream) 0%, var(--panel-cream) 70%, rgba(251, 248, 230, 0.7) 88%, rgba(251, 248, 230, 0) 100%);
  }
  .outcome-photo {
    position: absolute;
    left: 0;
    right: 0;
    top: 700px;
    bottom: 0;
    background:
      radial-gradient(ellipse 70% 45% at 50% 10%, var(--sun-gold) 0%, rgba(246, 223, 160, 0.6) 35%, rgba(246, 223, 160, 0) 75%),
      linear-gradient(180deg, rgba(239, 201, 164, 0) 0%, var(--sky-clear) 18%, var(--interior-mid) 55%, var(--interior-deep) 100%);
  }
  .top-rule {
    position: absolute;
    left: 198px;
    top: 46px;
    width: 376px;
    height: 2px;
    background: var(--ink-dark);
  }
  .book-title {
    position: absolute;
    left: 74px;
    width: 624px;
    top: 92px;
    margin: 0;
    text-align: center;
    font-family: "Cinzel", "Times New Roman", serif;
    font-weight: 600;
    color: var(--title-navy);
    text-transform: uppercase;
  }
  .book-title .line { display: block; white-space: nowrap; }
  .book-title .line-top { font-size: 112px; line-height: 126px; }
  .book-title .line-middle { font-size: 78px; line-height: 116px; color: var(--title-blue); font-weight: 500; }
  .book-title .line-bottom { font-size: 112px; line-height: 126px; }
  .divider {
    position: absolute;
    left: 0;
    width: 772px;
    top: 493px;
    display: flex;
    justify-content: center;
    align-items: center;
    gap: 18px;
  }
  .divider .dash { width: 22px; height: 2px; background: var(--ink-dark); }
  .divider .emblem {
    width: 34px;
    height: 34px;
    border-radius: 50%;
    background: var(--title-blue);
  }
  .subtitle {
    position: absolute;
    left: 74px;
    width: 624px;
    top: 562px;
    margin: 0;
    text-align: center;
    font-family: "EB Garamond", "Georgia", serif;
    font-weight: 600;
    font-size: 34px;
    line-height: 48px;
    color: var(--ink-dark);
  }
  .author-name {
    position: absolute;
    left: 0;
    width: 772px;
    top: 1126px;
    margin: 0;
    text-align: center;
    font-family: "EB Garamond", "Georgia", serif;
    font-weight: 500;
    font-size: 42px;
    color: var(--author-white);
  }
</style>
</head>
<body>
  <main class="cover">
    <div class="storm-sky" role="img" aria-label="Storm clouds at the top clearing into a warm sunrise sky"></div>
    <div class="title-panel"></div>
    <div class="outcome-photo" role="img" aria-label="Happy family laughing together in an open convertible, driving into golden sunrise light on a calm country road"></div>

    <div class="top-rule"></div>
    <h1 class="book-title">
      <span class="line line-top">Sunrise</span>
      <span class="line line-middle">Over Quiet</span>
      <span class="line line-bottom">Fields</span>
    </h1>

    <div class="divider">
      <span class="dash"></span>
      <span class="emblem" role="img" aria-label="Small ship's wheel emblem"></span>
      <span class="dash"></span>
    </div>

    <p class="subtitle">Steering Through<br>Every Crash Claim</p>

    <p class="author-name">Author Name</p>
  </main>
</body>
</html>
```